Website on Hubspot CMS -Boutique consulting firm focused on the events and event tech industries

Design website for our business using Hubspot CMS. Some pages already done. We would like those tweaked to match your recommended design. We also would like landing pages created for four business services offerings. We have a color palette and logo.

Our current website can be found here: www.qlvadvisors.co

QLV Advisors has four service lines:
1. Outsourced Sales
2. Harbor Ledger Strategic Consulting
3. Gridweave Strategic Consulting
4. QLV VIP

Target Market(s)

event organizers, media companies, corporate event marketers, event tech organizations

Industry/Entity Type

Consulting

Coding

Coded - Design and coding required

Number of Pages Required

5+ page

Font styles to use
Sans Serif

Requirements
Must have
• This will be a website built using Hubspot CMS. If you are not familiar with this, please do not participate as we will not be able to use your designs.
SEO optimized
Landing pages with lead capture leading to content downloads
Each service line needs its own page/s with cta's
Highly visual, modern, bold
Navigational areas: Home, Services, Resources, Events, Blog, About Us
Content formats: video, podcasts, content downloads
Will need at least 4 landing pages in addition to the website for each service line plus templates in case we need to update with new copy
We have or own color palette and logo as well as logos for Harbor Ledger and Gridweave. Those colors must be used.
Font can be modified
We need to have a conversation with the designer that is chosen to go over each service line and also understand what kind of images we should be uploading.
Nice to have
• We would really like the site to reflect the following words:
Bold
Future focused
Results oriented
Hyper focused on the events and event technology sectors (sub sectors: corporate event marketers and B2B media companies).
Should not have
• Flat one page design

```html
<!DOCTYPE html>
<html lang="en">
<head>
<meta charset="utf-8">
<title>QLV Advisors – Home Page</title>
<link rel="stylesheet" href="https://fonts.googleapis.com/css2?family=Poppins:wght@300;400;500;600;700&display=swap">
<style>
:root{
  --orange:#fc4a0a;
  --ink:#1d1d1f;
  --text:#6b6e75;
  --muted:#9a9da4;
  --ghost:#e6e7ea;
  --soft:#f5f6f8;
  --line:#d9dbe0;
  --navy:#2f3f56;
  --white:#ffffff;
}
*{margin:0;padding:0;box-sizing:border-box}
html,body{width:1200px;height:1200px;overflow:hidden;background:var(--white)}
body{font-family:'Poppins',sans-serif;color:var(--ink)}
.board{position:absolute;left:0;top:0;width:1932px;height:1932px;transform:scale(0.62112);transform-origin:0 0;overflow:hidden;background:var(--white)}
.abs{position:absolute}
.band{position:absolute;left:0;top:0}
.title-rule{left:0;top:185px;width:185px;height:4px;background:var(--orange)}
.ghost-word{left:278px;top:62px;font-size:198px;font-weight:600;color:var(--ghost);letter-spacing:6px;line-height:1}
.page-title{left:325px;top:150px;font-size:56px;font-weight:700;color:#111;letter-spacing:1px}
.panel{position:absolute;background:var(--white);box-shadow:0 4px 18px rgba(0,0,0,.12);overflow:hidden}
.panel-home{left:27px;top:375px;width:923px;height:1527px}
.panel-more{left:980px;top:83px;width:922px;height:1762px}
.brand{position:absolute;display:flex;align-items:baseline;gap:3px;color:var(--orange);font-weight:400}
.brand b{font-weight:400;font-size:26px;letter-spacing:-1px}
.brand span{font-size:7px}
.nav a{position:absolute;top:20px;font-size:11px;color:#444;text-decoration:none}
.nav a.active{color:var(--orange)}
.social{position:absolute;width:14px;height:14px;background:#9da0a6;border-radius:2px}
.eyebrow{font-size:12px;color:var(--orange);font-weight:500}
.rule{position:absolute;height:2px;width:32px;background:var(--orange)}
.h1{font-size:17px;font-weight:500;line-height:21px;color:var(--ink)}
.p{font-size:9.5px;line-height:14.5px;color:var(--text);font-weight:300}
.btn-fill{position:absolute;background:var(--orange);color:#fff;font-size:11px;font-weight:500;display:flex;align-items:center;justify-content:center}
.btn-line{position:absolute;border:1px solid var(--orange);color:var(--orange);font-size:9.5px;display:flex;align-items:center;justify-content:center;background:#fff}
.section-title{position:absolute;width:100%;text-align:center;font-size:15.5px;font-weight:500;color:var(--ink)}
.center-rule{position:absolute;left:50%;margin-left:-16px;height:2px;width:32px;background:var(--orange)}
.center-p{position:absolute;text-align:center;font-size:9.5px;line-height:14.5px;color:var(--text);font-weight:300}
.bullets{position:absolute;font-size:9.5px;line-height:15px;color:var(--text);font-weight:300}
.bullets i{display:inline-block;width:5px;height:5px;border-radius:50%;background:var(--orange);margin-right:3px;vertical-align:1px}
.svc{position:absolute;width:252px}
.svc-icon{width:46px;height:46px;border:2.5px solid var(--orange);border-radius:50%;margin-bottom:10px}
.svc h3{font-size:12px;font-weight:600;margin-bottom:8px;color:var(--ink)}
.svc p{font-size:9px;line-height:14.5px;color:var(--text);font-weight:300;text-align:justify}
.more-link{font-size:9.5px;color:var(--orange);margin-top:12px}
.photo{position:absolute}
.checks{position:absolute;font-size:9.5px;color:var(--text);font-weight:300}
.checks div{height:21.5px;display:flex;gap:5px}
.checks svg{margin-top:2px}
.video{position:absolute;left:0;top:389px;width:922px;height:385px;background:radial-gradient(ellipse at 35% 30%,#c03cd2 0%,transparent 40%),radial-gradient(ellipse at 75% 60%,#4b2bd0 0%,transparent 55%),linear-gradient(120deg,#6a1fc2,#3b1fa8 45%,#8a2ad6 70%,#3a1b9e)}
.card{position:absolute;top:921px;width:131px;height:162px;border:1.5px solid var(--line);background:#fff;text-align:center}
.avatar{width:58px;height:58px;border-radius:50%;margin:13px auto 14px;border:2px solid #f2c9b8}
.card h4{font-size:8.5px;font-weight:500;color:var(--ink)}
.card small{display:block;font-size:6px;color:var(--text);margin-top:2px}
.card .icons{position:absolute;top:128px;left:0;width:100%;display:flex;justify-content:center;gap:10px}
.card .icons i{width:15px;height:15px;border:1px solid var(--line);border-radius:50%}
.card .icons i.hot{border-color:var(--orange)}
.partner{position:absolute;top:1330px;width:58px;height:28px;border:2px solid #c9ccd2;border-radius:4px}
.footer{position:absolute;left:0;top:1432px;width:922px;height:330px;background:var(--navy);color:#c6ccd6}
.fcol{position:absolute;top:38px}
.fcol h5{font-size:12px;font-weight:500;color:#fff;margin-bottom:20px}
.fcol div{font-size:7.5px;line-height:9px;color:#aeb6c2;margin-bottom:14px;width:90px}
.fsoc{display:inline-block;width:14px;height:14px;background:#b7bdc7;border-radius:2px;margin-right:7px}
</style>
</head>
<body>
<div class="board">

  <svg class="band" width="1932" height="1932" viewBox="0 0 1932 1932" aria-hidden="true">
    <polygon points="0,960 1684,0 1932,0 1932,750 210,1932 0,1932" fill="#fc4a0a"/>
  </svg>

  <div class="abs title-rule"></div>
  <svg class="abs" style="left:175px;top:122px" width="130" height="130" viewBox="0 0 130 130" aria-hidden="true">
    <rect x="29" y="29" width="72" height="72" transform="rotate(45 65 65)" fill="none" stroke="#fc4a0a" stroke-width="13"/>
  </svg>
  <div class="abs ghost-word">HOME</div>
  <div class="abs page-title">HOME PAGE</div>

  <section class="panel panel-home">
    <div class="brand" style="left:180px;top:8px"><b>QLV</b><span>advisors</span></div>
    <nav class="nav">
      <a class="active" style="left:332px">Home</a>
      <a style="left:383px">Services</a>
      <a style="left:445px">Resources</a>
      <a style="left:518px">Blog</a>
      <a style="left:560px">About</a>
    </nav>
    <i class="social" style="left:654px;top:18px"></i>
    <i class="social" style="left:678px;top:18px"></i>
    <i class="social" style="left:702px;top:18px"></i>
    <i class="social" style="left:726px;top:18px"></i>

    <svg class="abs" style="left:0;top:48px" width="923" height="290" viewBox="0 0 923 290" aria-hidden="true">
      <path d="M0 0H923V262Q461 355 0 262Z" fill="#f5f6f8"/>
    </svg>

    <div class="abs eyebrow" style="left:182px;top:108px">Welcome to QLV</div>
    <div class="rule" style="left:182px;top:130px"></div>
    <div class="abs h1" style="left:182px;top:138px">Modernize Your Harbor Ledger™.<br>Get More Customers.</div>
    <div class="abs p" style="left:182px;top:186px;width:210px">Lorem ipsum dolor sit amet, consectetuer adipiscing elit, sed diam nonum</div>
    <div class="btn-fill" style="left:182px;top:231px;width:97px;height:22px">Get Started →</div>
    <div class="photo" role="img" aria-label="Two desktop monitors showing a growth chart above an open hand" style="left:463px;top:120px;width:292px;height:165px;background:linear-gradient(135deg,#e9ebef 0%,#2d3a44 30%,#3f5560 60%,#dfe2e6 100%);border-radius:6px"></div>
    <svg class="abs" style="left:457px;top:330px" width="8" height="12" viewBox="0 0 8 12" aria-hidden="true"><path d="M4 1V10M1 7L4 10L7 7" stroke="#333" fill="none" stroke-width="1.2"/></svg>

    <div class="section-title" style="top:380px">About Us</div>
    <div class="center-rule" style="top:408px"></div>
    <div class="center-p" style="left:261px;top:421px;width:400px">QLV Advisors helps event and media companies as well as the technology partners that support them modernize revenue organizations and future proof their businesses.</div>
    <div class="btn-line" style="left:413px;top:483px;width:97px;height:22px">More about us</div>

    <svg class="abs" style="left:0;top:545px" width="923" height="880" viewBox="0 0 923 880" aria-hidden="true">
      <path d="M0 35Q461 -25 923 35V880H0Z" fill="#f5f6f8"/>
    </svg>
    <div class="section-title" style="top:598px">Our services</div>
    <div class="center-rule" style="top:626px"></div>
    <div class="center-p" style="left:261px;top:640px;width:400px">QLV Advisors has four service lines:</div>
    <div class="bullets" style="left:300px;top:662px"><div><i></i>The Harbor Ledger™ Construct</div><div><i></i>Outsourced Sales</div></div>
    <div class="bullets" style="left:466px;top:662px"><div><i></i>Gridweave Strategic Consulting</div><div><i></i>QLV VIP</div></div>

    <div class="svc" style="left:182px;top:757px">
      <div class="svc-icon"></div>
      <h3>The Harbor Ledger™ Construct</h3>
      <p>For clients who wish to deploy part or all of The Harbor Ledger strategy, we work side-by-side with you to understand your current organizational structure, customer base, product offering, sales structure and processes, sales alignment with marketing and product teams, customer journey, KPIs and metrics as well as customer success and sales enablement. We develop plans that you can execute in a phased approach that won't disrupt current sales traction but allows you to move towards optimal and sustainable sales acceleration and have an impact on the bottom line.</p>
      <div class="more-link">Learn more ›</div>
    </div>
    <div class="svc" style="left:461px;top:757px">
      <div class="svc-icon"></div>
      <h3>Gridweave Strategic Consulting</h3>
      <p>We work with customers to map out profitable digital strategies to complement and enhance live events. Our expertise lies in identifying new revenue streams that allow for superior customer experience, greater share of wallet, longer customer lifetime value and better customer retention and expansion. Services include organizational modeling, virtual and hybrid event strategy, P&amp;L development, product innovation, go-to-market strategy, and sales enablement.</p>
      <div class="more-link">Learn more ›</div>
    </div>
    <div class="svc" style="left:182px;top:1072px">
      <div class="svc-icon"></div>
      <h3>Outsourced Sales</h3>
      <p>We offer outsourced sales leadership, individual contributor and customer success support for event tech, event organizations, and associations who have rapid go-to-market demands with a new product launch, resource gaps, or who are entering a new geographic market. Our team can handle the entire sales lifecycle from initial impression to lead qualification and through to close. We are uniquely positioned to quickly ramp, offer guidance on sales processes, positioning, and pitch. We use an account based selling approach and have a database of over 1,000 decision-makers across independent and association run events.</p>
      <div class="more-link">Learn more ›</div>
    </div>
    <div class="svc" style="left:461px;top:1072px">
      <div class="svc-icon"></div>
      <h3><span style="color:var(--orange)">QLV</span> VIP</h3>
      <p>We model and roll out 21st century sales organizations designed to meet our clients' new customer demands. We work with clients to navigate today's more complex selling environment and adopt and upskill teams quickly in order to capture more wallet-share and increase LTV of their customers. We focus on Demand Generation, Sales Enablement, Sales Operations, SDR, AE and CSM eco-system to create a cohesive, integrated and well-oiled Harbor Ledger machine. Modeling includes current and future growth mapping based on our client's 12 to 18 month plans, sales pacing against key product sets, ratio of new business acquisition versus retention and expansion, and current state of the business as well as business environment.</p>
      <div class="more-link">Learn more ›</div>
    </div>

    <div class="photo" role="img" aria-label="Team photo in a bright office" style="left:200px;top:1478px;width:241px;height:60px;background:linear-gradient(90deg,#eef0e8,#c9b49a 50%,#f3f1ec)"></div>
    <div class="abs" style="left:461px;top:1473px;font-size:16px;font-weight:500">We are the best Agency</div>
    <div class="abs" style="left:461px;top:1500px;font-size:9.5px;line-height:14.5px;color:var(--orange);font-weight:300;width:260px">Lorem ipsum dolor sit amet, consectetuer adipiscing elit, sed diam nonummy nibh euimod tincidunt</div>
  </section>

  <section class="panel panel-more">
    <div class="photo" role="img" aria-label="Hands stacked together in a team gesture" style="left:395px;top:160px;width:46px;height:133px;background:linear-gradient(180deg,#e5e2dc,#c9c2b8)"></div>
    <div class="photo" role="img" aria-label="Close-up of hands stacked together in an office" style="left:199px;top:20px;width:242px;height:145px;background:linear-gradient(135deg,#dfe6d6,#c89a7c 50%,#e9ebe6)"></div>
    <div class="photo" role="img" aria-label="Colleagues talking in a modern office" style="left:181px;top:170px;width:214px;height:148px;background:linear-gradient(135deg,#2b3444,#4a5b72 50%,#c8a24a 75%,#2f3a4a);border:3px solid #fff"></div>

    <div class="abs" style="left:461px;top:14px;font-size:16px;font-weight:500">We are the best Agency</div>
    <div class="abs" style="left:461px;top:41px;width:262px;font-size:9.5px;line-height:14.5px;color:var(--orange);font-weight:300">Lorem ipsum dolor sit amet, consectetuer adipiscing elit, sed diam nonummy nibh euimod tincidunt</div>
    <div class="abs p" style="left:461px;top:76px;width:252px;text-align:justify">Lorem ipsum dolor sit amet, consectetuer adipiscing elit, sed diam nonummy nibh euismod tincidunt ut laoreet dolore magna aliquam erat volutpat. Ut wisi enim ad minim veniam.</div>
    <div class="checks" style="left:461px;top:141px">
      <div><svg width="8" height="8" viewBox="0 0 8 8"><path d="M1 4L3 6.5L7 1" stroke="#fc4a0a" stroke-width="1.6" fill="none"/></svg>Lorem ipsum dolor sit amet, consectetuer</div>
      <div><svg width="8" height="8" viewBox="0 0 8 8"><path d="M1 4L3 6.5L7 1" stroke="#fc4a0a" stroke-width="1.6" fill="none"/></svg>Nonummy nibh euismod tincidu</div>
      <div><svg width="8" height="8" viewBox="0 0 8 8"><path d="M1 4L3 6.5L7 1" stroke="#fc4a0a" stroke-width="1.6" fill="none"/></svg>Sit amet, consectetuer adipiscing elit</div>
      <div><svg width="8" height="8" viewBox="0 0 8 8"><path d="M1 4L3 6.5L7 1" stroke="#fc4a0a" stroke-width="1.6" fill="none"/></svg>Orem ipsum dolor sit amet</div>
    </div>
    <div class="btn-line" style="left:461px;top:249px;width:89px;height:22px">Contacts ⟶</div>

    <div class="video" role="img" aria-label="Video still of abstract flowing purple and violet shapes"></div>
    <svg class="abs" style="left:434px;top:548px" width="54" height="54" viewBox="0 0 54 54" aria-label="Play video">
      <circle cx="27" cy="27" r="25" fill="none" stroke="#fff" stroke-width="1.2" opacity=".8"/>
      <circle cx="27" cy="27" r="20" fill="#fff"/>
      <path d="M24 20L32 27L24 34Z" fill="#fc4a0a"/>
    </svg>

    <div class="section-title" style="top:810px">Our Professional Team</div>
    <div class="center-rule" style="top:839px"></div>
    <div class="center-p" style="left:266px;top:852px;width:390px">Lorem ipsum dolor sit amet, consectetuer adipiscing elit, sed diam nonummy nibh euismod tincidunt ut laoreet dolore magna aliquam erat volutpat. Ut wisi enim ad minim veniam, quis nostrud exerci</div>

    <div class="card" style="left:181px"><div class="avatar" role="img" aria-label="Portrait of Mara L. Vestby" style="background:linear-gradient(135deg,#e8a46c,#b76a3c)"></div><h4>Mara L. Vestby</h4><small>Founder &amp; Managing Partner</small><div class="icons"><i class="hot"></i><i></i></div></div>
    <div class="card" style="left:324px"><div class="avatar" role="img" aria-label="Portrait of Tessa Rowan" style="background:linear-gradient(135deg,#d98a6a,#f3e6dc)"></div><h4>Tessa Rowan</h4><small>Vice President Business Development</small><div class="icons"><i></i><i></i></div></div>
    <div class="card" style="left:467px"><div class="avatar" role="img" aria-label="Portrait of Owen Dale" style="background:linear-gradient(135deg,#3b3733,#8c7a6a)"></div><h4>Owen Dale</h4><small>Inside Sales Executive</small><div class="icons"><i></i><i></i></div></div>
    <div class="card" style="left:610px"><div class="avatar" role="img" aria-label="Portrait of Lena Marsh" style="background:linear-gradient(135deg,#d6b07a,#8a6a4c)"></div><h4>Lena Marsh</h4><small>Inside Sales Executive</small><div class="icons"><i></i><i></i></div></div>

    <div class="btn-line" style="left:412px;top:1116px;width:97px;height:22px">Learn more ›</div>

    <svg class="abs" style="left:0;top:1195px" width="922" height="240" viewBox="0 0 922 240" aria-hidden="true">
      <path d="M0 32Q461 -20 922 32V240H0Z" fill="#f5f6f8"/>
    </svg>
    <div class="section-title" style="top:1248px">Our Partners</div>
    <div class="abs" style="left:0;width:922px;top:1287px;text-align:center;font-size:9.5px;color:var(--orange)">Learn more ›</div>
    <div class="partner" style="left:181px"></div>
    <div class="partner" style="left:281px"></div>
    <div class="partner" style="left:381px"></div>
    <div class="partner" style="left:481px"></div>
    <div class="partner" style="left:581px"></div>
    <div class="partner" style="left:681px"></div>

    <footer class="footer">
      <div class="brand" style="left:181px;top:40px"><b style="font-size:34px">QLV</b><span style="font-size:8px;color:#fff">advisors</span></div>
      <div class="abs" style="left:181px;top:98px;width:210px;font-size:7.5px;line-height:13px;color:#aeb6c2;font-weight:300">Lorem ipsum dolor sit amet, consectetuer adipiscing elit, sed diam nonummy nibh euismod tincidunt ut laoreet dolore magna aliquam erat volutpat. Ut wisi enim ad minim veniam</div>
      <div class="fcol" style="left:413px"><h5>Services</h5><div>All services</div><div>The Harbor Ledger™ Construct</div><div>Gridweave Strategic Consulting</div><div>Outsourced Sales</div><div>QLV VIP</div></div>
      <div class="fcol" style="left:522px"><h5>Resources</h5><div>Virtual Reset 1.0</div><div>Virtual Reset 2.0</div><div>Virtual Reset 3.0</div><div>The Harbor Ledger™</div><div>Best practices for virtual event</div><div>Level up</div></div>
      <div class="fcol" style="left:631px"><h5>Contact Us</h5><div>Hint question 1</div><div>Hint question 2</div><div>Hint question 3</div><div>QLV Advisors, Inc. Port Alder, FL</div><div>Phone number</div>
        <div style="width:120px;margin-top:14px"><i class="fsoc" style="background:var(--orange)"></i><i class="fsoc"></i><i class="fsoc"></i><i class="fsoc"></i></div></div>
      <div class="abs" style="left:359px;top:261px;width:163px;height:22px;border:1px solid #8a94a3;background:#3a4a61;font-size:6.5px;color:#98a2b0;padding:7px 0 0 26px">Find something</div>
      <div class="abs" style="left:526px;top:261px;width:37px;height:22px;background:var(--orange);color:#fff;font-size:12px;text-align:center;line-height:20px">⟶</div>
      <div class="abs" style="left:181px;top:305px;width:560px;height:1px;background:#46556b"></div>
      <div class="abs" style="left:0;width:922px;top:314px;text-align:center;font-size:6.5px;color:#8f99a8">Copyright © 2021 Fennrow. All rights reserved.</div>
    </footer>
  </section>
</div>
</body>
</html>
```